People Analytics Company needs Web Design and CSS

We need a refreshed design for a People Analytics company called VOMTA Systems Inc. We have developed an online survey tool that our immediate need is to make it look snazzier for upcoming pilots with prospective companies. Dark Blue and Orange are the colors we like to use but the survey should be "neutral" - we don't want to influence any responses based on colors.

Target Market(s)

Enterprise Users

Industry/Entity Type

It Company

Coding

Coded - Design and coding required

Number of Pages Required

3 page

Font styles to use
Sans Serif

Colors
0556a4
f37122

Requirements
Must have
• User friendly way of responding to survey questions that is suitable for a tablet (fat fingers). Drag and Drop is also very hard on tablet.
• Neutral look and feel to reduce any potential respondent bias.
• Colors consistent with brand colors attached in document.
• Minimal scrolling is best.
Should not have
• Too many colors.

```html
<!DOCTYPE html>
<html lang="en">
<head>
<meta charset="utf-8">
<title>VOMTA Systems Inc. – Ranking</title>
<link href="https://fonts.googleapis.com/css2?family=Quicksand:wght@400;500;700&family=Ubuntu:wght@400&display=swap" rel="stylesheet">
<style>
:root{
  --orange:#f37122;
  --blue:#0556a4;
  --blue-light:#5a8ec5;
  --navy:#0b1535;
  --brown:#96441a;
  --cream:#f7f7f1;
  --band:#f2f2e6;
  --text:#555;
  --white:#fff;
}
*{margin:0;padding:0;box-sizing:border-box}
html,body{width:1200px;height:1140px;overflow:hidden;background:var(--white)}
body{position:relative;font-family:"Quicksand",sans-serif;color:var(--text)}
.abs{position:absolute}
.site-header{left:0;top:0;width:1200px;height:97px;background:var(--cream)}
.nav-btn{top:0;width:84px;height:97px;display:flex;align-items:center;justify-content:center;color:var(--white);font-size:11px;font-weight:500;letter-spacing:1.2px}
.nav-home{left:171px;background:var(--orange)}
.nav-logout{left:944px;background:var(--blue)}
.brand{left:520px;top:28px;width:160px;height:40px;display:flex;align-items:center;gap:8px;justify-content:center}
.brand-mark{width:18px;height:18px;background:var(--navy)}
.brand-name{font-weight:700;font-size:17px;color:var(--navy)}
.intro{left:171px;top:140px;width:857px;height:68px;background:var(--band);text-align:center;padding-top:16px;font-size:12px;letter-spacing:1.1px;line-height:20px;color:#666}
.intro b{font-weight:700;color:#555}
.panel-head{height:57px;background:var(--cream);display:flex;align-items:center;justify-content:center;font-size:12px;letter-spacing:.8px;color:#555}
.panel-head b{font-weight:700;color:#333}
.choices{left:171px;top:252px;width:347px}
.choice{height:96.7px;position:relative;color:var(--white);padding:21px 0 0 21px}
.choice:nth-child(odd){background:var(--blue-light)}
.choice:nth-child(even){background:var(--blue)}
.tag{font-size:11px;font-weight:700;letter-spacing:1px;display:flex;align-items:center;gap:10px}
.tag::before{content:"";width:5px;height:5px;border-radius:50%;background:var(--white)}
.statement{font-family:"Ubuntu",sans-serif;font-size:12px;line-height:16.5px;margin-top:9px;width:250px;opacity:.95}
.drag{position:absolute;right:19px;top:32px;text-align:center;font-size:10px;font-weight:700;width:34px}
.drag svg{display:block;margin:0 auto 4px}
.ranking{left:625px;top:252px;width:403px;height:734px;background:var(--orange)}
.ranking .panel-head{position:absolute;left:0;top:0;width:403px}
.scale-label{left:80px;font-size:11px;font-weight:700;letter-spacing:1.2px;color:var(--white)}
.slot{left:80px;width:288px;height:75px;border:1px dashed rgba(255,255,255,.85);display:flex;align-items:center;justify-content:center;color:var(--white);font-size:9.5px;font-weight:500;letter-spacing:.8px}
.slot b{font-weight:700;margin-right:3px}
.slot.filled{background:var(--brown);display:block;padding:14px 0 0 24px;border-color:rgba(255,255,255,.5)}
.slot.filled .statement{width:250px;margin-top:7px;font-size:11.5px;line-height:15.5px}
.site-footer{left:0;top:1044px;width:1200px;height:96px;background:var(--navy)}
.copy{left:173px;top:41px;font-size:10px;font-weight:700;letter-spacing:.6px;color:var(--white)}
.copy span{color:var(--orange)}
.foot-mark{left:573px;top:19px;width:56px;height:56px;background:#3b4466;border-radius:3px}
.social{top:42px;width:10px;height:10px;border-radius:50%;background:#9aa0b5}
</style>
</head>
<body>
<header class="site-header abs">
  <a class="nav-btn nav-home abs">HOME</a>
  <div class="brand abs"><span class="brand-mark"></span><span class="brand-name">VOMTA Systems Inc.</span></div>
  <a class="nav-btn nav-logout abs">LOGOUT</a>
</header>

<section class="intro abs">
  We Would Now Like To Understand Which Of The Selections You Made Previously Are Most<br>
  <b>Important To Your Ability To Work Effectively.</b>
</section>

<section class="choices abs">
  <div class="panel-head">Please Rank The Chosen&nbsp;<b>7 Items</b></div>
  <div class="choice"><div class="tag">Attitudes :</div><p class="statement">It is better for a leader to share an opinion first to start a discussion.</p><div class="drag"><svg width="24" height="14" viewBox="0 0 24 14"><path d="M0 5h14V0l10 7-10 7V9H0z" fill="#fff"/></svg>DRAG</div></div>
  <div class="choice"><div class="tag">Attitudes :</div><p class="statement">It is better for a leader to share an opinion first to start a discussion.</p><div class="drag"><svg width="24" height="14" viewBox="0 0 24 14"><path d="M0 5h14V0l10 7-10 7V9H0z" fill="#fff"/></svg>DRAG</div></div>
  <div class="choice"><div class="tag">Attitudes :</div><p class="statement">It is better for a leader to share an opinion first to start a discussion.</p><div class="drag"><svg width="24" height="14" viewBox="0 0 24 14"><path d="M0 5h14V0l10 7-10 7V9H0z" fill="#fff"/></svg>DRAG</div></div>
  <div class="choice"><div class="tag">Attitudes :</div><p class="statement">It is better for a leader to share an opinion first to start a discussion.</p><div class="drag"><svg width="24" height="14" viewBox="0 0 24 14"><path d="M0 5h14V0l10 7-10 7V9H0z" fill="#fff"/></svg>DRAG</div></div>
  <div class="choice"><div class="tag">Attitudes :</div><p class="statement">It is better for a leader to share an opinion first to start a discussion.</p><div class="drag"><svg width="24" height="14" viewBox="0 0 24 14"><path d="M0 5h14V0l10 7-10 7V9H0z" fill="#fff"/></svg>DRAG</div></div>
  <div class="choice"><div class="tag">Attitudes :</div><p class="statement">It is better for a leader to share an opinion first to start a discussion.</p><div class="drag"><svg width="24" height="14" viewBox="0 0 24 14"><path d="M0 5h14V0l10 7-10 7V9H0z" fill="#fff"/></svg>DRAG</div></div>
  <div class="choice"><div class="tag">Attitudes :</div><p class="statement">It is better for a leader to share an opinion first to start a discussion.</p><div class="drag"><svg width="24" height="14" viewBox="0 0 24 14"><path d="M0 5h14V0l10 7-10 7V9H0z" fill="#fff"/></svg>DRAG</div></div>
</section>

<svg class="abs" style="left:546px;top:619px" width="50" height="50" viewBox="0 0 50 50" aria-hidden="true">
  <g fill="#c4c4c4">
    <circle cx="3" cy="24" r="2.6"/><circle cx="13" cy="24" r="2.6"/><circle cx="23" cy="24" r="2.6"/><circle cx="33" cy="24" r="2.6"/><circle cx="43" cy="24" r="2.6"/>
    <circle cx="25" cy="3" r="2.6"/><circle cx="34" cy="13" r="2.6"/><circle cx="34" cy="35" r="2.6"/><circle cx="25" cy="45" r="2.6"/>
  </g>
</svg>

<section class="ranking abs">
  <div class="panel-head">My Ranking Of What Is&nbsp;<b>Most Important</b>&nbsp;To Me</div>
  <svg class="abs" style="left:29px;top:83px" width="22" height="626" viewBox="0 0 22 626" aria-hidden="true">
    <defs><linearGradient id="fade" x1="0" y1="0" x2="0" y2="1"><stop offset="0" stop-color="#fff" stop-opacity=".9"/><stop offset="1" stop-color="#fff" stop-opacity=".25"/></linearGradient></defs>
    <path d="M11 0L22 15H16V611H22L11 626 0 611H6V15H0z" fill="url(#fade)"/>
  </svg>
  <div class="scale-label abs" style="top:86px">MOST IMPORTANT</div>
  <div class="slot filled abs" style="top:104px"><div class="tag">Attitudes :</div><p class="statement">It is better for a leader to share an opinion first to start a discussion.</p></div>
  <div class="slot abs" style="top:188px"><b>2nd</b> Important</div>
  <div class="slot abs" style="top:271px"><b>3rd</b> Important</div>
  <div class="slot abs" style="top:355px"><b>4th</b> Important</div>
  <div class="slot filled abs" style="top:438px"><div class="tag">Attitudes :</div><p class="statement">It is better for a leader to share an opinion first to start a discussion.</p></div>
  <div class="slot abs" style="top:522px"><b>6th</b> Important</div>
  <div class="slot abs" style="top:606px"><b>7th</b> Important</div>
  <div class="scale-label abs" style="top:701px">LEAST IMPORTANT</div>
</section>

<footer class="site-footer abs">
  <p class="copy abs">Copyrights © 2015. All Rights Reserved. <span>VOMTA.us</span></p>
  <div class="foot-mark abs" role="img" aria-label="VOMTA mark"></div>
  <span class="social abs" style="left:923px" aria-label="Social link"></span>
  <span class="social abs" style="left:954px" aria-label="Social link"></span>
  <span class="social abs" style="left:986px" aria-label="Social link"></span>
  <span class="social abs" style="left:1018px" aria-label="Social link"></span>
</footer>
</body>
</html>
```